High-End audio shop owner needs a business card

I need a personal Business Card for my Audio shop which exists since 1962. We offer high Quality brands, professional Attention and run our own repair-service-department. I look for a design which will be printed on high Quality paper and shall convey trust to the Client that we are very serious. Language is german.

```html
<!DOCTYPE html>
<html lang="de">
<head>
<meta charset="utf-8">
<title>Hi-Fi Talbach – Visitenkarte</title>
<link rel="stylesheet" href="https://fonts.googleapis.com/css2?family=Montserrat:wght@700&family=Questrial&display=swap">
<style>
  :root {
    --backdrop: #3b3c3f;
    --card: #161616;
    --orange: #f26b1d;
    --white: #f2f2f2;
    --muted: #d8d8d8;
  }
  * { box-sizing: border-box; margin: 0; padding: 0; }
  html, body { width: 1200px; height: 900px; overflow: hidden; }
  body {
    background: var(--backdrop);
    position: relative;
    font-family: "Questrial", "Century Gothic", sans-serif;
  }
  .card {
    position: absolute;
    left: 290px;
    width: 620px;
    height: 354px;
    background: var(--card);
    border-radius: 22px;
    overflow: hidden;
  }
  .card--front { top: 70px; }
  .card--back { top: 476px; }

  .brand {
    position: absolute;
    display: flex;
    align-items: center;
    gap: 12px;
    font-family: "Montserrat", "Arial", sans-serif;
    font-weight: 700;
    color: var(--orange);
    text-transform: uppercase;
    letter-spacing: 1px;
    white-space: nowrap;
  }
  .brand__mark {
    width: 0.7em;
    height: 0.7em;
    background: var(--orange);
  }
  .card--front .brand {
    font-size: 44px;
    left: 50%;
    top: 50%;
    transform: translate(-50%, -50%);
  }
  .card--back .brand {
    font-size: 28px;
    right: 48px;
    top: 44px;
  }

  .person {
    position: absolute;
    left: 74px;
    top: 118px;
  }
  .person__accent {
    position: absolute;
    left: -22px;
    top: 4px;
    width: 5px;
    height: 54px;
    background: var(--orange);
  }
  .person__name {
    font-family: "Montserrat", "Arial", sans-serif;
    font-weight: 700;
    font-size: 25px;
    color: var(--orange);
  }
  .person__role {
    font-size: 18px;
    color: var(--white);
    margin-top: 2px;
    padding-left: 12px;
  }

  .contact-rail {
    position: absolute;
    left: 54px;
    top: 176px;
    width: 1px;
    height: 160px;
    background: var(--orange);
  }
  .contact {
    position: absolute;
    left: 44px;
    top: 200px;
    list-style: none;
    color: var(--muted);
    font-size: 14.5px;
    line-height: 1.35;
  }
  .contact__item {
    display: flex;
    align-items: flex-start;
    gap: 14px;
    margin-bottom: 8px;
  }
  .contact__icon {
    flex: none;
    width: 21px;
    height: 19px;
    background: var(--orange);
    display: flex;
    align-items: center;
    justify-content: center;
    margin-top: 1px;
  }
  .contact__icon svg { width: 12px; height: 12px; }
  .contact__item--address .contact__icon { margin-top: 9px; }
</style>
</head>
<body>

  <section class="card card--front" aria-label="Vorderseite">
    <div class="brand"><span class="brand__mark"></span>Hi-Fi Talbach</div>
  </section>

  <section class="card card--back" aria-label="Rückseite">
    <div class="brand"><span class="brand__mark"></span>Hi-Fi Talbach</div>

    <div class="person">
      <span class="person__accent"></span>
      <p class="person__name">Lukas Brenner</p>
      <p class="person__role">General Manager</p>
    </div>

    <span class="contact-rail"></span>
    <ul class="contact">
      <li class="contact__item contact__item--address">
        <span class="contact__icon">
          <svg viewBox="0 0 12 12"><path d="M6 1a3.5 3.5 0 0 0-3.5 3.5C2.5 7 6 11 6 11s3.5-4 3.5-6.5A3.5 3.5 0 0 0 6 1z" fill="#fff"/><circle cx="6" cy="4.5" r="1.3" fill="#f26b1d"/></svg>
        </span>
        <span>Lindenweg 14<br>Auenfeld, 4821</span>
      </li>
      <li class="contact__item">
        <span class="contact__icon">
          <svg viewBox="0 0 12 12"><path d="M3 1.5l1.8 2.2-1 1.2a6 6 0 0 0 3.3 3.3l1.2-1 2.2 1.8-1 1.6C5.5 10.6 1.4 6.5 1.4 2.5z" fill="#fff"/></svg>
        </span>
        <span>02 5550 1962</span>
      </li>
      <li class="contact__item">
        <span class="contact__icon">
          <svg viewBox="0 0 12 12"><rect x="3" y="1" width="6" height="10" rx="1" fill="none" stroke="#fff" stroke-width="1.2"/><circle cx="6" cy="9.2" r="0.6" fill="#fff"/></svg>
        </span>
        <span>0411 555 019</span>
      </li>
      <li class="contact__item">
        <span class="contact__icon">
          <svg viewBox="0 0 12 12"><rect x="1" y="2.5" width="10" height="7" fill="none" stroke="#fff" stroke-width="1.2"/><path d="M1 2.5l5 4 5-4" fill="none" stroke="#fff" stroke-width="1.2"/></svg>
        </span>
        <span>kontakt@hifi-talbach.de</span>
      </li>
      <li class="contact__item">
        <span class="contact__icon">
          <svg viewBox="0 0 12 12"><circle cx="6" cy="6" r="4.6" fill="none" stroke="#fff" stroke-width="1.2"/><path d="M1.4 6h9.2M6 1.4c-2 2.5-2 6.7 0 9.2M6 1.4c2 2.5 2 6.7 0 9.2" fill="none" stroke="#fff" stroke-width="0.9"/></svg>
        </span>
        <span>www.hifi-talbach.de</span>
      </li>
    </ul>
  </section>

</body>
</html>
```